Covid-19 Mortgage Housing Market Coaching

I need a one page 8.5 x 11 printable infographic to describe the following:
Housing and Mortgage Market Coach
Through your Employer Home-ownership Benefit
The Coronavirus has resulted in an unprecedented Government coordination to reduce the spread of the virus, as such, has altered the way we live and work.
As each of us looks to the potential impact of the Coronavirus to our financial stability, it can be difficult to obtain trusted information to help make sound financial decisions.
As part of your employee home ownership program through your employer, you have access to this educational coaching on the below topics:
• What is happening in the stock market and why it is happening.
• Motivation behind Feds cutting rates and how that translates to the lending market.
• Discuss the future of interest rates.
• Discuss the future of the housing market. How will the spring and summer housing markets be effected?
• Everyone says to refinance now. Is that really in my best interest? Learn how to do a refinance analysis and determine if refinancing is right for you.
Having a better understanding of what is happening in the financial markets, with interest rates and the housing market can help you successfully navigate this rapidly evolving situation.
Please be sure that our phone number is prominently displayed 1-800-529-8172 and our web address www.brightkeylending.example

```html
<!DOCTYPE html>
<html lang="en">
<head>
<meta charset="utf-8">
<title>Housing and Mortgage Market Coaching</title>
<link href="https://fonts.googleapis.com/css2?family=Open+Sans:wght@400;600;700;800&display=swap" rel="stylesheet">
<style>
  :root {
    --teal: #1d5b6e;
    --teal-light: #cfe3ea;
    --red: #e8423f;
    --blue: #29abe2;
    --orange: #f9b122;
    --navy: #2a4d6e;
    --ink: #1f2a30;
    --white: #ffffff;
  }
  * { box-sizing: border-box; margin: 0; padding: 0; }
  html, body { width: 927px; height: 1200px; overflow: hidden; background: var(--white); }
  .sheet { position: relative; width: 927px; height: 1200px; font-family: "Open Sans", Arial, sans-serif; color: var(--ink); }

  .masthead { position: absolute; left: 0; top: 0; width: 927px; height: 177px; background: var(--teal); text-align: center; color: var(--white); }
  .masthead h1 { position: absolute; left: 0; right: 0; top: 54px; font-size: 33px; font-weight: 800; letter-spacing: 0.3px; }
  .masthead p { position: absolute; left: 0; right: 0; top: 118px; font-size: 20px; font-weight: 400; color: var(--teal-light); }

  .intro { position: absolute; left: 0; right: 0; top: 194px; text-align: center; font-size: 18.5px; font-weight: 600; }
  .rule { position: absolute; left: 0; top: 236px; width: 927px; height: 3px; background: var(--teal); }

  .contact-tab { position: absolute; left: 0; top: 492px; width: 394px; height: 463px; background: var(--teal); border-radius: 0 232px 232px 0; color: var(--white); }
  .contact-tab .phone { position: absolute; left: 22px; top: 150px; font-size: 39px; font-weight: 400; letter-spacing: 0.3px; }
  .contact-tab .web { position: absolute; left: 26px; top: 207px; font-size: 20px; font-weight: 600; }

  .step-number { position: absolute; font-size: 72px; font-weight: 400; color: var(--teal); line-height: 1; }
  .topic { position: absolute; border: 3px solid; background: var(--white); box-shadow: 2px 3px 4px rgba(0,0,0,0.25); display: flex; align-items: center; font-size: 12.5px; font-weight: 600; text-transform: uppercase; line-height: 1.55; }
  .topic--red { border-color: var(--red); }
  .topic--blue { border-color: var(--blue); }
  .topic--orange { border-color: var(--orange); }

  .icon-art { position: absolute; border-radius: 10px; }
  .footer-band { position: absolute; left: 0; top: 1174px; width: 927px; height: 26px; background: var(--teal); }
</style>
</head>
<body>
<main class="sheet">
  <header class="masthead">
    <h1>HOUSING AND MORTGAGE MARKET COACHING</h1>
    <p>THROUGH YOUR EMPLOYER HOME OWNERSHIP BENEFIT</p>
  </header>

  <p class="intro">YOU WILL HAVE ACCESS TO THIS EDUCATIONAL COACHING ON THE BELOW TOPICS</p>
  <div class="rule"></div>

  <aside class="contact-tab">
    <div class="phone">1-800-529-8172</div>
    <div class="web">www.brightkeylending.example</div>
  </aside>

  <span class="step-number" style="left:52px; top:330px;">1</span>
  <div class="icon-art" role="img" aria-label="Illustration of a colourful market chart" style="left:197px; top:280px; width:134px; height:110px; background: linear-gradient(90deg, var(--blue) 0%, var(--navy) 35%, var(--red) 65%, var(--orange) 100%);"></div>
  <div class="topic topic--red" style="left:61px; top:397px; width:416px; height:65px; padding-left:60px;">What is happening in the stock market<br>and why it is happening</div>

  <div class="icon-art" role="img" aria-label="Illustration of an orange arrow rising from a blue cloud" style="left:605px; top:364px; width:160px; height:110px; background: linear-gradient(180deg, var(--orange) 0%, #f7c25a 45%, var(--blue) 100%);"></div>
  <span class="step-number" style="left:414px; top:474px;">2</span>
  <div class="topic topic--blue" style="left:485px; top:482px; width:413px; height:63px; padding-left:32px;">Motivation behind feds cutting that<br>translates to the lending marketrates and how</div>

  <div class="icon-art" role="img" aria-label="Illustration of a money bag between up and down arrows" style="left:621px; top:606px; width:159px; height:118px; background: linear-gradient(90deg, var(--blue) 0%, var(--orange) 50%, var(--red) 100%);"></div>
  <span class="step-number" style="left:414px; top:722px;">3</span>
  <div class="topic topic--orange" style="left:485px; top:727px; width:412px; height:61px; padding-left:43px;">Discuss the future of interest rates</div>

  <div class="icon-art" role="img" aria-label="Illustration of three small houses" style="left:614px; top:810px; width:166px; height:117px; background: linear-gradient(135deg, var(--blue) 0%, var(--orange) 100%);"></div>
  <span class="step-number" style="left:414px; top:928px;">4</span>
  <div class="topic topic--blue" style="left:485px; top:932px; width:413px; height:63px; padding-left:43px;">Discuss the future of housing market</div>

  <span class="step-number" style="left:56px; top:968px;">5</span>
  <div class="icon-art" role="img" aria-label="Illustration of a money bag on a stepped podium" style="left:179px; top:932px; width:173px; height:109px; background: linear-gradient(180deg, var(--orange) 0%, var(--blue) 55%, var(--navy) 100%);"></div>
  <div class="topic topic--red" style="left:61px; top:1042px; width:416px; height:64px; padding-left:45px;">Learn how to do a refinance analysis<br>and determine if refinancing is right for you.</div>

  <footer class="footer-band"></footer>
</main>
</body>
</html>
```